Double Sided DL flyer - Moth Lantern Virtual Reality Escape rooms

We need a fun double sided DL flyer for our Virtual Reality escape rooms we have just opened in our VR centre aimed at customers 13+. Go to our page to see the current games and pictures and descriptions https://www.quillbarrowpk.com.au/book-online
Explore new realities.Our VR escape rooms allow you to experience a reality that is virtually impossible and challenge yourself in situations that would not normally be possible. From 1 to 4 players per game. Escape rooms are a tactile gaming experience where players work together to solve challenges using a variety of hints, clues, and puzzles to 'escape' a room within a time limit. Players have upto 60 minutes to finish the game. Can you escape?
PLEASE DO NOT USE PICTURES FROM THE OTHER PAGES ON THE WEB SITE AS THEY ARE OWNED BY QUILLBARROW> ONLY USE PICTURES ON THE PAGE ON THE LINK ABOVE, FOR OTHER PICTURE IDEAS WE USE NOLA MAX 7 VR HEADSETS, DRIFT TABS?, bring escape rooms and virtual reality together
i have added some pictures to brief that may be used or for ideas

Target Market(s)

teens and adults

Industry/Entity Type

Entertainment / Virtual Reality

Requirements
Must have
• must be fun, bright
Should not have
• open to all ideas as long as it has a fun vibe BUT MUST NOT HAVE PICTURES FROM OUR OTHER PAGES ON OUR WEB SITE AS THEY ARE COPYRIGHT NOT BELONGING TO MOTHLANTERN

```html
<!DOCTYPE html>
<html lang="en">
<head>
<meta charset="utf-8">
<title>Moth Lantern VR Escape Rooms – DL Flyer</title>
<link rel="stylesheet" href="https://fonts.googleapis.com/css2?family=Russo+One&family=Audiowide&family=Roboto:wght@400;500&family=Roboto+Condensed:wght@400;500&display=swap">
<style>
  :root {
    --page-bg: #5b5b5d;
    --navy-deep: #0a1a33;
    --navy-mid: #123a66;
    --navy-glow: #1c5a8c;
    --brand-violet: #6f7fd6;
    --cyan: #22c4ea;
    --pink: #e8268a;
    --white: #ffffff;
    --gold: #d9b15a;
  }
  * { box-sizing: border-box; margin: 0; padding: 0; }
  html, body { width: 753px; height: 1200px; overflow: hidden; }
  body {
    background: var(--page-bg);
    display: flex;
    align-items: center;
    justify-content: center;
    gap: 17px;
    font-family: "Roboto", Arial, sans-serif;
  }
  .flyer {
    position: relative;
    width: 350px;
    height: 740px;
    background: radial-gradient(ellipse at 50% 40%, var(--navy-glow) 0%, var(--navy-mid) 40%, var(--navy-deep) 100%);
    box-shadow: 0 8px 22px rgba(0,0,0,0.45);
    overflow: hidden;
    color: var(--white);
  }
  .brand {
    position: absolute;
    top: 38px; left: 0; right: 0;
    text-align: center;
  }
  .brand-mark {
    display: block;
    width: 40px; height: 40px;
    margin: 0 auto 10px;
    border-radius: 50%;
    background: var(--brand-violet);
  }
  .brand-name {
    font-family: "Russo One", sans-serif;
    font-size: 27px;
    letter-spacing: 1px;
    color: var(--brand-violet);
    line-height: 1;
  }
  .brand-tagline {
    margin-top: 6px;
    font-family: "Audiowide", sans-serif;
    font-size: 10px;
    letter-spacing: 6px;
    color: var(--brand-violet);
  }
  .hero {
    position: absolute;
    left: 0; right: 0;
  }
  .hero--tomb {
    top: 140px; height: 320px;
    background: linear-gradient(180deg, rgba(10,26,51,0) 0%, #5d6a72 30%, #b69a5e 48%, #3b4a55 70%, rgba(18,48,90,0.9) 100%);
  }
  .hero--key {
    top: 150px; height: 320px;
    background: radial-gradient(circle at 58% 35%, #f5dc8a 0%, #b98c3c 10%, rgba(40,110,170,0.55) 35%, rgba(18,58,102,0) 70%);
  }
  .content {
    position: absolute;
    left: 22px; right: 22px;
  }
  .flyer--tomb .content { top: 462px; }
  .flyer--key .content { top: 484px; }
  .headline {
    text-align: center;
    font-family: "Russo One", sans-serif;
    font-size: 22px;
    line-height: 1;
    color: var(--white);
  }
  .subhead {
    text-align: center;
    margin-top: 4px;
    font-family: "Audiowide", sans-serif;
    font-size: 16px;
    color: var(--cyan);
  }
  .intro {
    margin-top: 16px;
    font-size: 12px;
    line-height: 1.38;
    text-align: justify;
  }
  .details {
    margin-top: 14px;
    font-size: 11px;
    line-height: 1.3;
    color: var(--cyan);
  }
  .details strong { color: var(--white); font-weight: 400; }
  .flyer--tomb .details { width: 190px; font-family: "Audiowide", sans-serif; font-size: 10.5px; }
  .key-art {
    position: absolute;
    right: 28px; bottom: 62px;
    width: 100px; height: 70px;
    border-radius: 35px;
    background: radial-gradient(ellipse, #e2c06a 0%, #9c7430 55%, rgba(18,58,102,0) 75%);
  }
  .footer {
    position: absolute;
    left: 0; right: 0; bottom: 0;
    height: 52px;
    background: linear-gradient(90deg, var(--cyan) 0%, #6a7ad0 50%, var(--pink) 100%);
    display: flex;
    align-items: center;
    padding: 0 20px;
    font-family: "Roboto Condensed", sans-serif;
    font-size: 10.5px;
    line-height: 1.5;
  }
  .footer-col { display: flex; flex-direction: column; }
  .footer-col + .footer-col {
    margin-left: 8px;
    padding-left: 8px;
    border-left: 1px solid rgba(255,255,255,0.6);
  }
  .footer-label { font-weight: 500; }
  .footer-line { display: flex; align-items: center; gap: 4px; }
  .icon { width: 9px; height: 9px; flex: none; }
</style>
</head>
<body>

<article class="flyer flyer--tomb">
  <header class="brand">
    <span class="brand-mark"></span>
    <div class="brand-name">MOTHLANTERN</div>
    <div class="brand-tagline">ESCAPE ROOMS</div>
  </header>
  <div class="hero hero--tomb" role="img" aria-label="Explorers with torches inside an ancient Egyptian tomb beside a giant jackal-headed statue"></div>
  <section class="content">
    <h1 class="headline">MOTH LANTERN VIRTUAL</h1>
    <h2 class="subhead">REALITY ESCAPE ROOMS</h2>
    <p class="intro">A new addition to the Quillbarrow Sunshine coast centre , VIRTUAL REALITY escape Rooms. Games to suit 1-4 players, the sky isn't the limit with our escape rooms! Experience a virtual reality escape room in another world! Can you escape in time?</p>
    <p class="details">Details for games and info can be found here -VR Escape Rooms | Quillbarrow VR Suns <strong>(quillbarrowpk.com.au)</strong></p>
  </section>
  <div class="key-art" role="img" aria-label="Ornate golden skeleton key"></div>
  <footer class="footer">
    <div class="footer-col">
      <span class="footer-label">Located in the Quillbarrow Centre</span>
      <span class="footer-line">
        <svg class="icon" viewBox="0 0 10 10"><circle cx="5" cy="5" r="5" fill="#e8268a"/><circle cx="5" cy="4" r="1.6" fill="#fff"/></svg>
        27 Harbour Lane, Kellfield Q
      </span>
    </div>
    <div class="footer-col">
      <span class="footer-line">
        <svg class="icon" viewBox="0 0 10 10"><circle cx="5" cy="5" r="5" fill="#e8268a"/><path d="M3 3l1 0 .6 1.4-.6.5a3 3 0 001.1 1.1l.5-.6L7 6v1a1 1 0 01-1 .4A4 4 0 012.6 4 1 1 0 013 3z" fill="#fff"/></svg>
        1300555018
      </span>
      <span class="footer-line">
        <svg class="icon" viewBox="0 0 10 10"><circle cx="5" cy="5" r="5" fill="#e8268a"/><circle cx="5" cy="5" r="2.6" fill="none" stroke="#fff" stroke-width=".7"/><path d="M2.4 5h5.2M5 2.4v5.2" stroke="#fff" stroke-width=".6"/></svg>
        www.quillbarrowpk.com.au
      </span>
    </div>
  </footer>
</article>

<article class="flyer flyer--key">
  <header class="brand">
    <span class="brand-mark"></span>
    <div class="brand-name">MOTHLANTERN</div>
    <div class="brand-tagline">ESCAPE ROOMS</div>
  </header>
  <div class="hero hero--key" role="img" aria-label="Glowing golden key floating above an open hand among blue light particles"></div>
  <section class="content">
    <h1 class="headline">MOTH LANTERN VIRTUAL</h1>
    <h2 class="subhead">REALITY ESCAPE ROOMS</h2>
    <p class="intro">A new addition to the Quillbarrow Sunshine coast centre , VIRTUAL REALITY escape Rooms. Games to suit 1-4 players, the sky isn't the limit with our escape rooms! Experience a virtual reality escape room in another world! Can you escape in time?</p>
    <p class="details">Details for games and info can be found here -VR Escape Rooms | Quillbarrow VR Suns <strong>(quillbarrowpk.com.au)</strong></p>
  </section>
  <footer class="footer">
    <div class="footer-col">
      <span class="footer-label">Located in the Quillbarrow Centre</span>
      <span class="footer-line">
        <svg class="icon" viewBox="0 0 10 10"><circle cx="5" cy="5" r="5" fill="#e8268a"/><circle cx="5" cy="4" r="1.6" fill="#fff"/></svg>
        27 Harbour Lane, Kellfield Q
      </span>
    </div>
    <div class="footer-col">
      <span class="footer-line">
        <svg class="icon" viewBox="0 0 10 10"><circle cx="5" cy="5" r="5" fill="#e8268a"/><path d="M3 3l1 0 .6 1.4-.6.5a3 3 0 001.1 1.1l.5-.6L7 6v1a1 1 0 01-1 .4A4 4 0 012.6 4 1 1 0 013 3z" fill="#fff"/></svg>
        1300555018
      </span>
      <span class="footer-line">
        <svg class="icon" viewBox="0 0 10 10"><circle cx="5" cy="5" r="5" fill="#e8268a"/><circle cx="5" cy="5" r="2.6" fill="none" stroke="#fff" stroke-width=".7"/><path d="M2.4 5h5.2M5 2.4v5.2" stroke="#fff" stroke-width=".6"/></svg>
        www.quillbarrowpk.com.au
      </span>
    </div>
  </footer>
</article>

</body>
</html>
```